Etiketten für Ätherische Öle, Extrakte und Speiseöle gesucht
Zielgruppe
Wir verkaufen natürlich Produkte. Ätherische öle, Extrakte, Speise öle.
Wir verkaufen im Webshop, Kaufrix und auch im Betrieb.
https://www.natur-feyo.com
Wir verkaufen hauptsächlich innerhalb Italiens und Deutschland daher doppel sprachig.
Aufgabenstellung
Guten Tag
Bitte verwenden Sie! : * beispiel_10_ml_etikett_nachbau.jpg *
Da mir die kleinste Größe die wichtigste ist habe ich ein beispiel Hochgeladen. Das kleinste Etikett lässt sich öffnen und daher sind nur 7 cm ersichtlich und man muss das Etikett aufmachen.
Habe ein Beispiel Hochgeladen. Aber bitte einfach kreativ sein. *Anhang: beispiel Etikett*
Sobald ich eine Art vom kelinsten habe würde ich dies für die 2 anderen Größen übernehmen aber das man Sie irgendwie gut unterscheiden kann da dies dann komplett andere Produkte (Extrakte/Speise öl) sein werden.
Erstellung von drei unterschiedlichen Größen von Etiketten mit folgenden Eigenschaften:
Am wichtigsten ist mir das kleinste Etikett da dies auch am schwersten ist daher habe ich die anderen Größen nun gelöscht!
• 10 ml Länge: 155 mm Breite: 32 mm.
Brauche 3 unterschiedliche Grund Farben: z. B. Ätherische Öle (Grün) Extrakte (Rot) Speiseöle (gelb). Die Farben lasse ich sie entscheiden.
Die Etiketten müssen 2 Sprachen (Deutsch / Italienisch) sein deshalb muss dieses berücksichtigt werden.
Anbei finden Sie:
• Logo (Bild Logo)
• Beispiel Text ätherische Öle
• Bilder der aktuellen Flaschen
Unter https://www.natur-feyo.com/de finden Sie meine Seite
Anmerkung: Im Anhang: *Back*
Habe ich mein Logo mit Firmennamen ; Natur des Holmberg Viktor
Da ich jedoch nicht alle Produkte im biologischen Anbau habe und mein Logo zu miss Verständnis führen könnte habe ich ein Bildliches Logo gemacht das ich fortan auf meinen Produkten haben möchte. Im besonderes dieses Grün das in beiden vorhanden ist versuche ich zu integrieren.
Habe selbst ein Etikett designet das aber sehr unprofessionell wirkt aber dieses Grüne das ich gerne als merkmal unterbringen würde.
Siehe Anhang: neemöl

```html
<!DOCTYPE html>
<html lang="de">
<head>
<meta charset="utf-8">
<title>Lavendel Fein – Etikett 10 ml</title>
<link rel="stylesheet" href="https://fonts.googleapis.com/css2?family=Roboto+Condensed:wght@400;700&family=Sriracha&family=Varela+Round&family=Roboto:wght@400;500&display=swap">
<style>
  :root {
    --page: #ffffff;
    --ink: #262626;
    --purple: #5b2d86;
    --leaf: #5aa52a;
    --leaf-light: #9cd03a;
    --lime: #d9e84a;
    --yellow: #eef27a;
    --olive: #8a8a1c;
    --label-white: #fafbf7;
  }
  * { box-sizing: border-box; margin: 0; padding: 0; }
  html, body { width: 1200px; height: 1200px; overflow: hidden; background: var(--page); }
  .canvas { position: relative; width: 1200px; height: 1200px; }

  .label {
    position: absolute; left: 50px; top: 387px; width: 1100px; height: 425px;
    background: var(--label-white); overflow: hidden;
    box-shadow: 0 2px 10px rgba(0,0,0,.12);
    font-family: "Roboto Condensed", sans-serif; color: var(--ink);
  }
  .swoosh-art {
    position: absolute; inset: 0;
    background:
      radial-gradient(ellipse 40% 75% at 46% 40%, rgba(255,255,255,.95) 0 30%, transparent 60%),
      linear-gradient(100deg, var(--leaf) 0%, var(--leaf-light) 18%, var(--lime) 32%, var(--olive) 42%, var(--yellow) 48%, rgba(255,255,255,.6) 62%, var(--label-white) 72%);
  }
  .leaf-art {
    position: absolute; left: 560px; bottom: -40px; width: 560px; height: 90px;
    border-radius: 50% 50% 0 0;
    background: linear-gradient(90deg, rgba(156,208,58,0) 0%, var(--leaf-light) 55%, var(--leaf) 100%);
  }

  .safety-text {
    position: absolute; left: 23px; top: 26px; width: 235px;
    font-size: 10.5px; line-height: 13.5px;
  }
  .safety-text p + p { margin-top: 7px; }
  .producer { position: absolute; left: 23px; top: 197px; width: 240px; font-size: 10.5px; line-height: 13.5px; }
  .producer .name { font-weight: 700; }
  .batch { position: absolute; left: 23px; top: 375px; font-size: 10.5px; }
  .shelf-life { position: absolute; left: 23px; top: 391px; display: flex; gap: 4px; font-size: 10.5px; line-height: 12px; }
  .shelf-life svg { width: 18px; height: 18px; flex: none; }

  .brand-mark {
    position: absolute; left: 470px; top: 70px; display: flex; align-items: center; gap: 8px;
    font-family: "Roboto Condensed", sans-serif; font-weight: 700; font-size: 20px; color: var(--leaf);
  }
  .brand-mark .dot { width: 16px; height: 16px; border-radius: 50%; background: var(--leaf); }

  .product-title {
    position: absolute; left: 384px; width: 320px; top: 205px; text-align: center;
  }
  .product-name { font-family: "Sriracha", cursive; font-size: 66px; line-height: 70px; color: var(--purple); }
  .product-grade {
    font-family: "Varela Round", sans-serif; font-size: 19px; letter-spacing: 5px;
    color: var(--purple); font-weight: 700; margin-top: 2px;
  }
  .title-rule { width: 78px; height: 3px; background: var(--purple); margin: 16px auto 12px; }
  .botanical { font-family: "Roboto", sans-serif; font-size: 16.5px; line-height: 17px; color: var(--purple); }

  .usage {
    position: absolute; left: 807px; top: 30px; width: 285px;
    font-size: 10.5px; line-height: 14px;
  }
  .usage p { margin-bottom: 5px; }
  .usage strong { font-weight: 700; }
  .usage .gap { margin-top: 16px; }
</style>
</head>
<body>
<div class="canvas">
  <section class="label" aria-label="Etikett Lavendel Fein 10 ml">
    <div class="swoosh-art" role="img" aria-label="Geschwungene Farbbänder in Grün und Gelb"></div>
    <div class="leaf-art" role="img" aria-label="Grünes Blatt am unteren Rand"></div>

    <div class="safety-text">
      <p>Nur in der angegeben Verdünnung anwenden! Nicht in die Augen oder auf die Schleimhäute bringen! Außer Reichweite von Kindern lagern. Abgefüllt in Italien</p>
      <p>Da usare solo diluito come da indicazione! Evitare il contatto con occhi e mucose! Tenere fuori dalla portata dei bambini. Imbottigliato in Italy</p>
    </div>

    <div class="producer">
      <p class="name">Natur des Holmberg Viktor</p>
      <p>Feldweg 14</p>
      <p>I-39020 Feyo</p>
      <p>IVA: IT04518260391</p>
      <p>CF: HLMVKT88L12B204Q</p>
      <p>Tel: +39 0471/208815 Handy: 3405129876</p>
      <p>www.natur-feyo.com</p>
      <p>info@natur-feyo.com</p>
    </div>

    <p class="batch">LottoNummer/CH nummer: 123456</p>
    <div class="shelf-life">
      <svg viewBox="0 0 18 18" aria-hidden="true"><path d="M2 12 Q9 4 15 8" fill="none" stroke="var(--purple)" stroke-width="2"/><path d="M12 5 L16 8 L12 11" fill="none" stroke="var(--purple)" stroke-width="2"/></svg>
      <p>Haltbar bis <strong>12 Monate</strong><br>nach der Öffnung</p>
    </div>

    <div class="brand-mark"><span class="dot"></span><span>Natur Feyo</span></div>

    <div class="product-title">
      <h1 class="product-name">Lavendel</h1>
      <p class="product-grade">FEIN</p>
      <div class="title-rule"></div>
      <p class="botanical">Lavanda vera</p>
      <p class="botanical">Lavandula angustifolia</p>
    </div>

    <div class="usage">
      <p><strong>100% olio essenziale naturale.</strong> Cosmetico aromatico per la cura del corpo.</p>
      <p><strong>Modo d'uso:</strong> Come olio da massaggio o olio per il corpo: versare max. 15 gocce in 50ml di liquido p.es. olio di mandorla. Come bagnoschiuma: aggiungere 8-15 gocce versare nell acqua del bagno.</p>
      <p><strong>Ingredients:</strong> Lavandula angustifolia oil, Limonene*, Linalool*, geraniol*<br>*natürliche Bestandteile des etherischen Öls<br>* Olio essenziale con sostanze naturali</p>
      <p class="gap"><strong>100% natürliches etherisches Öl.</strong><br>Aroma-Kosmetikum zur Körperpflege.</p>
      <p><strong>Anwendung:</strong> Als Haut- u. Massageöl max 15 Tr. Mit 50 ml z.B. Mandelöl mischen. Als Badezusatz 8-15 Tr. Auf 4 EßI. Sahne oder Milch ins Badewasser geben.</p>
    </div>
  </section>
</div>
</body>
</html>
```